Business Card Design

We are looking for a double sided business card.

On one side would be our logo

On the Other Side

Martin Kolby
Sales and Marketing

Phone/Text Logo and 530-418-2763
Email Logo and info@plumvalepets.com
Website Logo and www.plumvalepets.com
Facebook Logo and plumvale pets
Instagram Logo and plumvale_pets

Target Market(s)

Pet owners

Contact Information for Business Card

In project description

Requirements
Must have
• Logo

```html
<!DOCTYPE html>
<html lang="en">
<head>
<meta charset="utf-8">
<title>Plumvale Pets — Business Card</title>
<link href="https://fonts.googleapis.com/css2?family=Lato:wght@300;400;700;900&display=swap" rel="stylesheet">
<style>
  :root{
    --stage:#18191b;
    --stage-light:#2c2d30;
    --card:#242426;
    --orange:#f7901e;
    --amber:#ffc20e;
    --white:#f2f2f2;
    --grey:#c9c9c9;
  }
  *{margin:0;padding:0;box-sizing:border-box}
  html,body{width:1200px;height:952px;overflow:hidden}
  body{
    background:radial-gradient(ellipse at 60% 55%,var(--stage-light) 0%,var(--stage) 70%);
    font-family:"Lato",sans-serif;
    position:relative;
  }
  .card{
    position:absolute;width:540px;height:309px;background:var(--card);
    border-radius:4px;overflow:hidden;
    box-shadow:0 18px 40px rgba(0,0,0,.55);
  }
  /* logo side */
  .card--logo{left:600px;top:150px}
  .tab{position:absolute;width:110px;height:34px;border-radius:8px;
    background:linear-gradient(90deg,var(--orange),var(--amber),var(--orange))}
  .tab--top{left:26px;top:-10px}
  .tab--bottom{right:26px;bottom:-10px}
  .brand{position:absolute;left:0;right:0;top:110px;text-align:center}
  .brand-row{display:flex;align-items:center;justify-content:center;gap:12px}
  .brand-mark{width:30px;height:30px;background:var(--orange);border-radius:3px}
  .brand-name{font-weight:900;font-size:34px;letter-spacing:1px;color:var(--white);text-transform:uppercase}
  .brand-web{margin-top:14px;font-size:10px;font-weight:700;letter-spacing:3px;color:var(--orange);text-transform:uppercase}
  /* contact side */
  .card--contact{left:60px;top:490px}
  .emblem{position:absolute;left:-70px;top:70px;width:250px;height:250px;border-radius:50%;
    background:radial-gradient(circle at 40% 40%,var(--amber),var(--orange) 60%,#b85f0c)}
  .person{position:absolute;left:34px;top:28px}
  .person-name{font-weight:900;font-size:24px;color:var(--orange);text-transform:uppercase;letter-spacing:.5px}
  .person-role{font-weight:300;font-size:15px;color:var(--white);margin-top:2px;padding-bottom:6px;
    border-bottom:1.5px solid var(--white);display:inline-block}
  .contacts{position:absolute;left:250px;top:150px;list-style:none}
  .contacts li{display:flex;align-items:center;gap:9px;font-size:14px;color:var(--white);height:26px}
  .icon{width:18px;height:18px;border-radius:3px;background:var(--orange);display:flex;align-items:center;justify-content:center}
  .icon--amber{background:var(--amber)}
  .icon--grey{background:var(--grey)}
  .icon svg{width:12px;height:12px}
  .icon-pair{display:flex;gap:3px}
</style>
</head>
<body>
  <section class="card card--logo" aria-label="Logo side">
    <div class="tab tab--top"></div>
    <div class="tab tab--bottom"></div>
    <div class="brand">
      <div class="brand-row">
        <span class="brand-mark"></span>
        <span class="brand-name">Plumvale Pets</span>
      </div>
      <div class="brand-web">www.plumvalepets.com</div>
    </div>
  </section>

  <section class="card card--contact" aria-label="Contact side">
    <div class="emblem" role="img" aria-label="Large brand emblem decoration"></div>
    <div class="person">
      <div class="person-name">Martin Kolby</div>
      <div class="person-role">Sales and Marketing</div>
    </div>
    <ul class="contacts">
      <li><span class="icon"><svg viewBox="0 0 24 24"><path fill="#242426" d="M6.6 10.8a15 15 0 0 0 6.6 6.6l2.2-2.2c.3-.3.7-.4 1-.2 1.1.4 2.3.6 3.6.6.6 0 1 .4 1 1V20c0 .6-.4 1-1 1A17 17 0 0 1 3 4c0-.6.4-1 1-1h3.5c.6 0 1 .4 1 1 0 1.3.2 2.5.6 3.6.1.3 0 .7-.2 1z"/></svg></span>530-418-2763</li>
      <li><span class="icon"><svg viewBox="0 0 24 24"><rect x="3" y="6" width="18" height="12" fill="none" stroke="#242426" stroke-width="2"/><path d="M3 6l9 7 9-7" fill="none" stroke="#242426" stroke-width="2"/></svg></span>info@plumvalepets.com</li>
      <li><span class="icon icon--amber"><svg viewBox="0 0 24 24"><path fill="#242426" d="M6 3l13 8-6 1.5L16 20l-3 1-3-7.5L6 17z"/></svg></span>www.plumvalepets.com</li>
      <li><span class="icon-pair"><span class="icon icon--grey"></span><span class="icon icon--grey"></span></span>plumvale pets</li>
    </ul>
  </section>
</body>
</html>
```